New Web Design Project

See attachments on the content and concept. Very important that the flow of the tiers stand out

Target Market(s)

Food and Beverage Manufacturing

Industry/Entity Type

Food and Beverage

Coding

Coded - Design and coding required

Number of Pages Required

3 page

Colors
0054AA
0677BA
7BADD7
CADEEF
E8F1F8

```html
<!DOCTYPE html>
<html lang="en">
<head>
<meta charset="utf-8">
<title>Northline Consulting Group — SQF Consulting</title>
<link href="https://fonts.googleapis.com/css2?family=Montserrat:wght@400;500;600;700;800&family=Syncopate:wght@400&display=swap" rel="stylesheet">
<style>
:root{
  --blue:#0054AA;
  --navy:#0B3F86;
  --deep:#073170;
  --mid:#0677BA;
  --sky:#7BADD7;
  --pale:#CADEEF;
  --mist:#E8F1F8;
  --ink:#1B2B45;
  --text:#3E4B5E;
  --white:#ffffff;
}
*{box-sizing:border-box;margin:0;padding:0}
html,body{width:1200px;height:4699px;overflow:hidden}
body{font-family:'Montserrat',sans-serif;color:var(--ink);background:var(--white);position:relative}
.abs{position:absolute}
/* header */
.site-header{position:absolute;left:0;top:0;width:1200px;height:73px;background:var(--white)}
.brand{position:absolute;left:104px;top:12px;display:flex;align-items:center;gap:12px}
.brand-dot{width:46px;height:46px;border-radius:50%;border:3px solid var(--blue)}
.brand-name{font-weight:700;font-size:18px;color:var(--blue);line-height:1.1}
.brand-sub{font-weight:600;font-size:11px;color:var(--blue)}
.nav{position:absolute;left:464px;top:25px;display:flex;gap:46px;font-size:14px;color:var(--text);font-weight:500}
.nav-cta{position:absolute;left:910px;top:10px;width:190px;height:46px;border-radius:23px;background:var(--navy);color:#fff;font-size:12.5px;font-weight:700;display:flex;align-items:center;justify-content:center}
/* hero */
.hero{position:absolute;left:0;top:73px;width:1200px;height:651px;background:linear-gradient(115deg,#0A4C9E 0%,#0054AA 55%,#0A4390 100%)}
.eyebrow-light{position:absolute;left:122px;top:138px;font-family:'Syncopate',sans-serif;font-size:13px;color:#fff;letter-spacing:.5px}
.hero h1{position:absolute;left:122px;top:165px;width:540px;font-size:28px;line-height:39px;font-weight:700;color:#fff;text-transform:uppercase;letter-spacing:-.2px}
.hero h1 span{display:block;white-space:nowrap}
.hero-copy{position:absolute;left:122px;top:302px;width:420px;font-size:14.5px;line-height:20px;color:#E6EEF8}
.btn{position:absolute;height:50px;border-radius:25px;font-size:14px;font-weight:700;display:flex;align-items:center;justify-content:center}
.btn-white{background:#fff;color:var(--navy)}
.btn-outline{border:2px solid #fff;color:#fff}
.btn-navy{background:var(--navy);color:#fff}
.btn-ghost{border:2px solid var(--pale);color:var(--navy);background:#fff}
/* stats */
.stats{position:absolute;left:77px;top:666px;width:1054px;height:127px;background:#fff;box-shadow:0 6px 24px rgba(0,40,100,.12);display:flex}
.stat{flex:1;display:flex;flex-direction:column;align-items:center;justify-content:center;border-right:1px solid var(--pale);margin:22px 0}
.stat:last-child{border:none}
.stat-num{font-size:38px;font-weight:700;color:var(--blue);line-height:1}
.stat-label{font-size:14px;font-weight:600;color:var(--blue);margin-top:12px}
/* section heads */
.eyebrow{position:absolute;left:0;width:1200px;text-align:center;font-family:'Syncopate',sans-serif;font-size:13px;color:var(--blue)}
.section-title{position:absolute;left:0;width:1200px;text-align:center;font-size:31px;font-weight:700;color:var(--ink);text-transform:uppercase;line-height:38px}
.section-title .accent{color:var(--blue)}
.section-lead{position:absolute;left:180px;width:840px;text-align:center;font-size:15.5px;line-height:21px;color:var(--text)}
/* services */
.service{position:absolute;width:330px}
.service h3{font-size:17px;font-weight:600;color:var(--ink);margin-bottom:6px}
.service p{font-size:11.5px;line-height:16px;color:var(--text)}
.service.left{text-align:right}
.svc-icon{position:absolute;width:60px;height:60px;border-radius:50%;background:var(--navy);display:flex;align-items:center;justify-content:center}
.connector{position:absolute;left:599px;width:2px;background:var(--navy)}
.connector::after{content:"";position:absolute;left:-4px;bottom:-5px;width:10px;height:10px;border-radius:50%;background:var(--navy)}
/* why */
.why{position:absolute;left:0;top:1550px;width:1200px;height:945px;background:var(--mist)}
.photo{position:absolute}
.benefit{position:absolute;left:610px;width:540px;display:flex;gap:22px}
.benefit-icon{width:70px;height:70px;flex:none;display:flex;align-items:center;justify-content:center}
.benefit h4{font-size:17px;font-weight:700;color:var(--ink);margin:6px 0 6px}
.benefit p{font-size:11px;line-height:16px;color:var(--text)}
/* steps */
.step{position:absolute;border:2px solid var(--pale);border-radius:8px;background:#fff;text-align:center}
.step-num{position:absolute;left:0;width:100%;font-size:62px;font-weight:800;color:var(--mist)}
.step h4{position:absolute;left:0;width:100%;font-size:17px;font-weight:700;color:var(--ink)}
.step p{position:absolute;left:26px;width:200px;font-size:11.5px;line-height:16px;color:var(--text)}
.step-icon{position:absolute;left:70px;width:114px;height:114px;border-radius:50%;border:3px solid var(--navy);display:flex;align-items:center;justify-content:center;background:#fff}
.flow-line{position:absolute;width:2px;background:var(--navy)}
/* testimonial */
.testimonial{position:absolute;left:80px;top:3243px;width:1062px;height:405px;border-radius:10px;background:linear-gradient(180deg,#DCE8F4 0%,#EAF2F9 100%)}
.quote-mark{position:absolute;left:0;width:100%;top:38px;text-align:center;font-size:120px;line-height:120px;font-weight:800;color:var(--navy)}
.quote{position:absolute;left:90px;width:882px;top:152px;text-align:center;font-size:24px;line-height:32px;font-weight:500;color:var(--navy)}
.cite{position:absolute;left:0;width:100%;top:278px;text-align:center;font-size:17px;font-weight:600;color:var(--navy)}
.badges{position:absolute;left:115px;top:3680px;width:990px;display:flex;justify-content:space-between;align-items:center}
.badge{display:flex;align-items:center;gap:12px;font-size:16px;font-weight:600;color:var(--ink)}
/* cta */
.cta-eyebrow{position:absolute;left:119px;top:3858px;font-size:13px;color:var(--text);font-weight:500}
.cta-title{position:absolute;left:119px;top:3888px;font-size:40px;font-weight:800;color:var(--navy)}
.cta-copy{position:absolute;left:119px;top:3958px;width:460px;font-size:17.5px;line-height:25px;color:var(--text)}
/* footer */
.site-footer{position:absolute;left:0;top:4323px;width:1200px;height:376px;background:linear-gradient(120deg,#0A3F88,#0054AA)}
.foot-brand{position:absolute;left:138px;top:90px;display:flex;align-items:center;gap:14px}
.foot-brand .brand-dot{border-color:#fff;width:50px;height:50px}
.foot-brand .brand-name,.foot-brand .brand-sub{color:#fff}
.foot-about{position:absolute;left:140px;top:172px;width:360px;font-size:13px;line-height:19px;color:#E1EAF6}
.foot-col{position:absolute;top:90px}
.foot-col h5{font-size:20px;font-weight:700;color:#fff;padding-bottom:10px;border-bottom:1px solid rgba(255,255,255,.45);width:162px;margin-bottom:14px}
.foot-col li{list-style:none;font-size:13.5px;color:#fff;line-height:25px}
.contact li{display:flex;align-items:center;gap:12px;line-height:33px}
.contact .dot{width:22px;height:22px;border-radius:50%;background:#fff;display:inline-block}
.copyright{position:absolute;left:0;top:340px;width:100%;text-align:center;font-size:12px;color:#E1EAF6}
.foot-rule{position:absolute;left:70px;right:70px;top:318px;height:1px;background:rgba(255,255,255,.25)}
</style>
</head>
<body>

<header class="site-header">
  <div class="brand">
    <span class="brand-dot"></span>
    <div><div class="brand-name">Northline Consulting Group</div><div class="brand-sub">Food Safety &amp; SQF Certification</div></div>
  </div>
  <nav class="nav"><span>Services</span><span>Benefits</span><span>Process</span><span>Contact</span></nav>
  <div class="nav-cta">Get SQF Consultation ↗</div>
</header>

<section class="hero">
  <div class="eyebrow-light">SQF ONLY · TECH DRIVEN</div>
  <h1><span>Hire a Tech-Driven SQF Team</span><span>That Carries You Across the</span><span>Certification Finish Line</span></h1>
  <p class="hero-copy">At Northline Consulting Group, we focus exclusively on SQF — combining real plant experience with smart technology so your team can stay focused on production while we handle the path to certification and beyond.</p>
  <div class="btn btn-white" style="left:122px;top:400px;width:228px">Get SQF Consultation ↗</div>
  <div class="btn btn-outline" style="left:363px;top:400px;width:218px">Explore Services ↗</div>
  <svg class="abs" style="left:640px;top:10px" width="490" height="570" viewBox="0 0 490 570" role="img" aria-label="Food production worker in hairnet and gloves inspecting packaged goods on a conveyor line">
    <defs>
      <linearGradient id="heroPhoto" x1="0" y1="0" x2="1" y2="1"><stop offset="0" stop-color="#E9EEF3"/><stop offset=".55" stop-color="#B8C7D6"/><stop offset="1" stop-color="#7E95AE"/></linearGradient>
      <linearGradient id="heroRing" x1="0" y1="0" x2="0" y2="1"><stop offset="0" stop-color="#C5D8EC"/><stop offset="1" stop-color="#5E8FC6"/></linearGradient>
    </defs>
    <path d="M245 5 L482 115 L482 345 Q482 480 245 565 Q8 480 8 345 L8 115 Z" fill="url(#heroRing)"/>
    <path d="M245 28 L460 128 L460 340 Q460 462 245 540 Q30 462 30 340 L30 128 Z" fill="url(#heroPhoto)"/>
  </svg>
</section>

<div class="stats">
  <div class="stat"><div class="stat-num">15+</div><div class="stat-label">Clients Onboarded</div></div>
  <div class="stat"><div class="stat-num">100%</div><div class="stat-label">SQF Focused</div></div>
  <div class="stat" style="flex:1.3">
    <svg width="46" height="46" viewBox="0 0 46 46" fill="none" stroke="#0054AA" stroke-width="2"><rect x="14" y="18" width="18" height="14" rx="2"/><circle cx="9" cy="9" r="5"/><circle cx="37" cy="9" r="5"/><circle cx="9" cy="40" r="4"/><circle cx="37" cy="40" r="4"/><path d="M14 13l4 5M32 13l-4 5M12 37l4-5M34 37l-4-5"/></svg>
    <div class="stat-label" style="margin-top:8px">Digital Platform Built Programs</div>
  </div>
  <div class="stat" style="flex:1.3">
    <svg width="56" height="40" viewBox="0 0 56 40" fill="none" stroke="#0054AA" stroke-width="2"><path d="M3 8 L22 5 L40 7 L53 6 L50 18 L44 24 L40 34 L34 28 L22 30 L12 26 L5 20 Z"/><path d="M14 12h22M12 18h28"/></svg>
    <div class="stat-label" style="margin-top:8px">US Nationwide Coverage</div>
  </div>
</div>

<!-- what we do -->
<div class="eyebrow" style="top:867px">WHAT WE DO</div>
<h2 class="section-title" style="top:895px">SQF Consulting, Implementation <span class="accent">&amp; Onboarding</span></h2>
<p class="section-lead" style="top:960px">We help food and beverage manufacturers achieve and maintain SQF certification with confidence, using practical programs and digital tools that work on the floor — not just on audit day.</p>

<div class="service left" style="left:66px;top:1058px"><h3>SQF Program Design</h3><p>We design your complete SQF system from scratch — HACCP/food safety plans, prerequisite programs, SOPs, forms, logs, and all required documentation tailored to your facility.</p></div>
<div class="service left" style="left:66px;top:1197px"><h3>Digital Platform Build</h3><p>We build your SQF program directly into modern food safety software like PlantTrack.io or SafeLedger.io — digitizing forms, checklists, monitoring logs, and workflows so your team runs paperless.</p></div>
<div class="service left" style="left:66px;top:1348px"><h3>Coaching &amp; Support</h3><p>After building your system, we coach your team to own and maintain it day-to-day. You run the program; we provide ongoing expert guidance so you stay audit-ready at all times.</p></div>

<div class="service" style="left:814px;top:1052px"><h3>Gap Assessments</h3><p>We evaluate where your facility stands against SQF requirements, identify gaps, and provide a clear roadmap to close them before your audit — no surprises on certification day.</p></div>
<div class="service" style="left:814px;top:1197px"><h3>Bilingual Team Support</h3><p>Our team in Central America supports Spanish-speaking employees within your operation — delivering training, documentation, and coaching in the language your floor team actually speaks.</p></div>
<div class="service" style="left:814px;top:1338px"><h3>Sanitation &amp; Regulatory</h3><p>From sanitation program design to environmental monitoring, we help you build internal capabilities that meet USDA, FDA, and FSMA requirements and reduce dependence on external contractors.</p></div>

<div class="svc-icon" style="left:420px;top:1072px"><svg width="30" height="30" viewBox="0 0 30 30" fill="none" stroke="#fff" stroke-width="2"><rect x="7" y="4" width="16" height="22" rx="2"/><path d="M11 11h8M11 16h8M11 21h5"/></svg></div>
<div class="svc-icon" style="left:420px;top:1202px"><svg width="30" height="30" viewBox="0 0 30 30" fill="none" stroke="#fff" stroke-width="2"><circle cx="15" cy="15" r="6"/><path d="M15 3v5M15 22v5M3 15h5M22 15h5M7 7l3 3M20 20l3 3M23 7l-3 3M10 20l-3 3"/></svg></div>
<div class="svc-icon" style="left:420px;top:1340px"><svg width="30" height="30" viewBox="0 0 30 30" fill="none" stroke="#fff" stroke-width="2"><circle cx="15" cy="9" r="4"/><circle cx="7" cy="13" r="3"/><circle cx="23" cy="13" r="3"/><path d="M8 26c0-5 3-8 7-8s7 3 7 8"/></svg></div>
<div class="svc-icon" style="left:740px;top:1074px"><svg width="30" height="30" viewBox="0 0 30 30" fill="none" stroke="#fff" stroke-width="2"><path d="M5 24V14M11 24V10M17 24V6M23 24V12"/></svg></div>
<div class="svc-icon" style="left:740px;top:1202px"><svg width="30" height="30" viewBox="0 0 30 30" fill="none" stroke="#fff" stroke-width="2"><circle cx="10" cy="10" r="4"/><circle cx="20" cy="10" r="4"/><path d="M3 25c0-5 3-8 7-8M27 25c0-5-3-8-7-8M10 25c0-4 2-6 5-6s5 2 5 6"/></svg></div>
<div class="svc-icon" style="left:740px;top:1342px"><svg width="30" height="30" viewBox="0 0 30 30" fill="none" stroke="#fff" stroke-width="2"><rect x="6" y="4" width="15" height="21" rx="2"/><path d="M10 10h7M10 15h7"/><circle cx="21" cy="21" r="5"/></svg></div>

<svg class="abs" style="left:500px;top:1112px" width="200" height="240" viewBox="0 0 200 240" aria-hidden="true">
  <circle cx="100" cy="118" r="98" fill="#fff" stroke="#CADEEF" stroke-width="6"/>
  <circle cx="100" cy="118" r="72" fill="none" stroke="#0B3F86" stroke-width="10"/>
  <circle cx="100" cy="118" r="54" fill="#E8F1F8"/>
</svg>

<div class="connector" style="top:1510px;height:68px"></div>

<!-- why -->
<section class="why">
  <div class="eyebrow" style="top:82px">WHY NORTHLINE CONSULTING</div>
  <h2 class="section-title" style="top:102px">Built for Small &amp; Mid-Size<br><span class="accent">Manufacturers</span></h2>
  <p class="section-lead" style="top:212px;left:170px;width:860px;font-size:17px;line-height:22px">You don't need to hire a full-time food safety director or figure out SQF alone. We bring the expertise and technology — you stay focused on production.<br>Consultant reviewing digital food safety compliance system in a manufacturing facility.</p>
  <svg class="photo" style="left:126px;top:347px" width="438" height="489" role="img" aria-label="Consultant in glasses reviewing a food safety compliance checklist on a tablet inside a manufacturing facility">
    <defs><linearGradient id="whyPhoto" x1="0" y1="0" x2="1" y2="1"><stop offset="0" stop-color="#DDE6EE"/><stop offset=".6" stop-color="#A9BCCF"/><stop offset="1" stop-color="#5F7C9D"/></linearGradient></defs>
    <rect width="438" height="489" rx="8" fill="url(#whyPhoto)"/>
  </svg>
  <div class="benefit" style="top:356px">
    <div class="benefit-icon"><svg width="70" height="70" viewBox="0 0 70 70"><path d="M35 3 L63 18 L63 50 L35 67 L7 50 L7 18 Z" fill="#0B3F86"/><circle cx="35" cy="32" r="11" fill="none" stroke="#fff" stroke-width="2"/><path d="M35 26v12M31 30h7" stroke="#fff" stroke-width="2"/></svg></div>
    <div><h4>Lower Cost Than a Full-Time Hire</h4><p>Get a complete SQF team — program design, digital implementation, and coaching — at a fraction of the cost of hiring a full-time SQF Practitioner.</p></div>
  </div>
  <div class="benefit" style="top:451px">
    <div class="benefit-icon"><svg width="54" height="54" viewBox="0 0 54 54" fill="none" stroke="#0B3F86" stroke-width="2"><path d="M27 6 L46 16 L27 26 L8 16 Z"/><path d="M8 26 L27 36 L46 26M8 36 L27 46 L46 36"/></svg></div>
    <div><h4>Your Program Lives in Software</h4><p>No more binders and spreadsheets. Your SQF system is built into PlantTrack.io or SafeLedger.io — organized, accessible, and always audit-ready.</p></div>
  </div>
  <div class="benefit" style="top:546px">
    <div class="benefit-icon"><svg width="54" height="54" viewBox="0 0 54 54" fill="none" stroke="#0B3F86" stroke-width="2"><circle cx="30" cy="20" r="9"/><circle cx="30" cy="20" r="4"/><path d="M6 38h10l8 4h14l8-6M6 46h10"/></svg></div>
    <div><h4>You Own It, We Support It</h4><p>We build the system and train your team. You maintain and run it day-to-day. We stay on call with coaching and advisory so you never feel stuck.</p></div>
  </div>
  <div class="benefit" style="top:645px">
    <div class="benefit-icon"><svg width="54" height="54" viewBox="0 0 54 54" fill="none" stroke="#0B3F86" stroke-width="2"><circle cx="27" cy="27" r="10"/><path d="M27 8v7M27 39v7M8 27h7M39 27h7M14 14l5 5M35 35l5 5M40 14l-5 5M19 35l-5 5"/></svg></div>
    <div><h4>Flexible, Low-Risk Engagement</h4><p>Start with a 3-month commitment, then go month-to-month. Cancel anytime with 30 days notice. We earn your business every month.</p></div>
  </div>
  <div class="benefit" style="top:742px">
    <div class="benefit-icon"><svg width="54" height="54" viewBox="0 0 54 54" fill="none" stroke="#0B3F86" stroke-width="2"><rect x="6" y="8" width="42" height="28" rx="3"/><path d="M12 16h10M12 22h14M30 16h12M30 22h10M20 44h14M27 36v8"/></svg></div>
    <div><h4>Bilingual Floor-Level Support</h4><p>With our Central America team, we provide training and documentation in Spanish so every member of your production team understands and follows the program.</p></div>
  </div>
</section>

<div class="connector" style="top:2462px;height:64px;background:var(--sky)"></div>

<!-- how it works -->
<div class="eyebrow" style="top:2566px">HOW IT WORKS</div>
<h2 class="section-title" style="top:2597px">From Discovery to <span class="accent">Certification</span></h2>
<p class="section-lead" style="top:2664px;font-size:17px">A clear, structured path that takes the guesswork out of SQF.</p>

<div class="step" style="left:97px;top:2756px;width:256px;height:390px">
  <div class="step-icon" style="top:40px"><svg width="48" height="48" viewBox="0 0 48 48" fill="none" stroke="#0B3F86" stroke-width="2.5"><path d="M12 6l7 8-4 5c2 5 6 9 11 11l5-4 8 7-4 6C22 39 9 26 6 12z"/><path d="M28 8c6 1 11 6 12 12M28 15c3 1 5 3 6 6"/></svg></div>
  <h4 style="top:180px">Discovery Call</h4>
  <p style="top:212px">We learn about your facility, your current systems, and where you are in the SQF journey. No pressure — just a conversation.</p>
  <div class="step-num" style="top:300px">01</div>
</div>
<div class="step" style="left:354px;top:2790px;width:256px;height:366px">
  <div class="step-num" style="top:8px">02</div>
  <h4 style="top:84px">Gap Assessment</h4>
  <p style="top:116px">We evaluate your facility against SQF requirements, identify what's missing, and give you a clear roadmap with priorities.</p>
  <div class="step-icon" style="top:222px"><svg width="48" height="48" viewBox="0 0 48 48" fill="none" stroke="#0B3F86" stroke-width="2.5"><rect x="8" y="6" width="24" height="34" rx="2"/><path d="M13 14h14M13 21h14M13 28h8"/><circle cx="33" cy="32" r="7"/><path d="M38 37l5 5"/></svg></div>
</div>
<div class="step" style="left:611px;top:2736px;width:256px;height:420px">
  <div class="step-icon" style="top:58px"><svg width="48" height="48" viewBox="0 0 48 48" fill="none" stroke="#0B3F86" stroke-width="2.5"><circle cx="24" cy="24" r="8"/><path d="M24 6v6M24 36v6M6 24h6M36 24h6M11 11l4 4M33 33l4 4M37 11l-4 4M15 33l-4 4"/></svg></div>
  <h4 style="top:198px">Build &amp; Implement</h4>
  <p style="top:230px">We design your SQF program and build it directly into your digital food safety platform — forms, logs, SOPs, HACCP plans, all of it.</p>
  <div class="step-num" style="top:340px">03</div>
</div>
<div class="step" style="left:868px;top:2770px;width:256px;height:374px">
  <div class="step-num" style="top:8px">04</div>
  <h4 style="top:84px">Coach &amp; Certify</h4>
  <p style="top:116px">We train your team, run mock audits, and prepare you for certification day. Then we stay on as your ongoing SQF advisory partner.</p>
  <div class="step-icon" style="top:228px"><svg width="50" height="48" viewBox="0 0 50 48" fill="none" stroke="#0B3F86" stroke-width="2.5"><rect x="18" y="6" width="26" height="20" rx="2"/><path d="M23 12h16M23 18h10"/><circle cx="14" cy="24" r="6"/><path d="M3 44c0-8 5-12 11-12s11 4 11 12"/></svg></div>
</div>

<svg class="abs" style="left:80px;top:2860px" width="1060" height="270" viewBox="0 0 1060 270" fill="none" stroke="#0B3F86" stroke-width="2" aria-hidden="true">
  <path d="M17 250V20M9 30l8-12 8 12"/><circle cx="17" cy="250" r="5" fill="#fff"/>
  <path d="M274 120V210M266 200l8 12 8-12"/>
  <path d="M531 110V12M523 22l8-12 8 12"/>
  <path d="M788 80V170M780 160l8 12 8-12"/>
  <circle cx="1045" cy="-32" r="5" fill="#fff"/>
</svg>

<!-- testimonial -->
<div class="testimonial">
  <div class="quote-mark">”</div>
  <p class="quote">"Northline Consulting Group didn't just hand us a binder. They built our entire SQF system into software and coached our team until we owned it. We passed our first audit with confidence."</p>
  <div class="cite">— SQF-Certified Manufacturing Client</div>
</div>

<div class="badges">
  <div class="badge"><svg width="40" height="40" viewBox="0 0 40 40"><circle cx="20" cy="20" r="17" fill="none" stroke="#0B3F86" stroke-width="2"/></svg>SQF Practitioner</div>
  <div class="badge"><span style="font-size:34px;color:var(--blue);font-weight:500;font-family:serif">6σ</span>Six Sigma Black Belt</div>
  <div class="badge"><svg width="44" height="40" viewBox="0 0 44 40" fill="none" stroke="#0054AA" stroke-width="2"><circle cx="22" cy="20" r="7"/><circle cx="7" cy="8" r="4"/><circle cx="37" cy="8" r="4"/><circle cx="7" cy="32" r="4"/><circle cx="37" cy="32" r="4"/><path d="M10 11l7 5M34 11l-7 5M10 29l7-5M34 29l-7-5"/></svg>Remote &amp; On-Site</div>
  <div class="badge"><svg width="42" height="40" viewBox="0 0 42 40" fill="none" stroke="#0054AA" stroke-width="2"><rect x="4" y="6" width="34" height="24" rx="2"/><path d="M10 14h14M10 20h10M28 14v10M15 36h12"/></svg>Digital-First</div>
</div>

<!-- cta -->
<div class="cta-eyebrow">GET SQF CONSULTING</div>
<h2 class="cta-title">READY TO TALK SQF?</h2>
<p class="cta-copy">Share a few details about your facility and where you are in the SQF journey. We'll follow up with a brief discovery call and a clear next step.</p>
<div class="btn btn-navy" style="left:119px;top:4063px;width:315px;height:54px;font-size:15px">Get My SQF Consultation ↗</div>
<div class="btn btn-ghost" style="left:119px;top:4137px;width:315px;height:54px;font-size:15px">Visit NorthlineOps.io ↗</div>
<svg class="abs" style="left:640px;top:3776px" width="480" height="530" viewBox="0 0 480 530" role="img" aria-label="Lab technician in a white coat reviewing data on a tablet in a blue-lit facility">
  <defs>
    <linearGradient id="ctaPhoto" x1="0" y1="0" x2="1" y2="1"><stop offset="0" stop-color="#8FB3D8"/><stop offset=".5" stop-color="#2F6FA8"/><stop offset="1" stop-color="#0D3566"/></linearGradient>
    <linearGradient id="ctaRing" x1="0" y1="0" x2="0" y2="1"><stop offset="0" stop-color="#E1ECF7"/><stop offset="1" stop-color="#A9C6E4"/></linearGradient>
  </defs>
  <path d="M240 4 L474 108 L474 322 Q474 448 240 526 Q6 448 6 322 L6 108 Z" fill="url(#ctaRing)"/>
  <path d="M240 26 L452 120 L452 318 Q452 432 240 504 Q28 432 28 318 L28 120 Z" fill="url(#ctaPhoto)"/>
</svg>

<footer class="site-footer">
  <div class="foot-brand">
    <span class="brand-dot"></span>
    <div><div class="brand-name" style="font-size:20px">Northline Consulting Group</div><div class="brand-sub" style="font-size:12px">Food Safety &amp; SQF Certification</div></div>
  </div>
  <p class="foot-about">Tech-driven SQF consulting for small and mid-size US food manufacturers. Based in Fresno, CA — serving clients across North America.</p>
  <div class="foot-col" style="left:578px">
    <h5>SERVICES</h5>
    <ul><li>SQF Program Design</li><li>Digital Platform Build</li><li>Coaching &amp; Support</li><li>Gap Assessments</li><li>Sanitation Programs</li></ul>
  </div>
  <div class="foot-col contact" style="left:840px">
    <h5>CONNECT</h5>
    <ul><li><span class="dot"></span>Email Us</li><li><span class="dot"></span>NorthlineOps.io</li><li><span class="dot"></span>Network Profile</li></ul>
  </div>
  <div class="foot-rule"></div>
  <div class="copyright">© 2026 Northline Consulting Group LLC. All rights reserved.</div>
</footer>

</body>
</html>
```